Push notification screens at app start up

We have an existing news publication app platform and are adding categories to push notifications.

We need two screens designed (each for Novaro, Tavlet and Morvelin for a total of 6d) that show when the app is first launched.

The workflow of our app:
0. app launch screen while webservices run (no work needed)
1. information screen to the user promoting the benefits of push notification with "Next" button. (see concept attached)
2. Push categories selection screen. This will have list of category types, with on/off switch.

"Select the categories that you wish to receive occasional notices:
Breaking News (on/off switch)
Local News (on/off switch)
Sports (on/off switch)
Local Events (on/off switch)
Weather Alerts (on/off switch)
Local Deals (on/off switch)"

"Enable these categories on the next screen."
"Next" button

Background:
When I was looking around at app designs, I came across this one (http://www.pixelvane.net/design/7148305) and I really liked it. We obviously have different features on our screen, but I’d like to have this same feel. The colors used in this design are perfect.

UPDATE: I do not mean to limit your design to match the layout as the one mentioned above. Please use your creativity for the layout.

Our standard font in Helvetica Neue.

Notes:
- our app is developed for all phone devices from Novaro 4 to Novaro 6, so designs should be thoughtful of vertical scrolling if needed.
- our app is developed for Tavlets, so we'll need designs completed as well. (We can finalize Novaro design first, then translate the design to Tavlet.)
- our app is developed for Morvelin phones (not tablets), so we'll need designs completed as well. (We can finalize Kvo design first, then translater to Morvelin UI design guidelines).

We hope to establish a good on-going relationship with the designer for as-needed work in the future.

Industry/Entity Type

News

Font styles to use
Other font styles liked:
• Helvetica Neue

Requirements
Must have
• Clean designs. No clutter.
Nice to have
• We would likely go with the standard on/off switches for both Kvo and Morvelin, but are open to small custom variations.

```html
<!DOCTYPE html>
<html lang="en">
<head>
<meta charset="utf-8">
<title>Notifications – Onboarding</title>
<link rel="stylesheet" href="https://fonts.googleapis.com/css2?family=Roboto:wght@300;400&display=swap">
<style>
  :root {
    --chrome: #5f6369;
    --chrome-text: #f2f3f4;
    --screen-bg: #f1f1f1;
    --title: #54585e;
    --body: #8a8d91;
  }
  html, body {
    margin: 0;
    padding: 0;
    width: 1200px;
    height: 2352px;
    overflow: hidden;
    background: var(--screen-bg);
    font-family: "Roboto", "Helvetica Neue", Helvetica, Arial, sans-serif;
    font-weight: 300;
  }
  .screen {
    position: relative;
    width: 1200px;
    height: 2352px;
    background: var(--screen-bg);
  }
  .status-bar {
    position: absolute;
    top: 0; left: 0;
    width: 1200px;
    height: 86px;
    color: var(--chrome-text);
    font-size: 32px;
    font-weight: 400;
    display: flex;
    align-items: center;
    z-index: 2;
  }
  .status-left { position: absolute; left: 24px; display: flex; align-items: center; gap: 12px; }
  .signal { display: flex; gap: 5px; }
  .signal span { width: 14px; height: 14px; border-radius: 50%; border: 2px solid var(--chrome-text); box-sizing: border-box; }
  .signal span.on { background: var(--chrome-text); }
  .status-time { position: absolute; left: 0; right: 0; text-align: center; }
  .status-right { position: absolute; right: 24px; display: flex; align-items: center; gap: 14px; }
  .battery { display: flex; align-items: center; }
  .battery-body { width: 64px; height: 27px; background: var(--chrome-text); border-radius: 4px; }
  .battery-tip { width: 5px; height: 11px; background: var(--chrome-text); margin-left: 2px; border-radius: 0 2px 2px 0; }
  .header-band {
    position: absolute;
    top: 0; left: 0;
    width: 1200px;
    height: 420px;
    z-index: 1;
  }
  .title {
    position: absolute;
    top: 490px;
    left: 0; right: 0;
    margin: 0;
    text-align: center;
    font-size: 48px;
    line-height: 60px;
    font-weight: 300;
    letter-spacing: 1px;
    color: var(--title);
  }
  .intro {
    position: absolute;
    top: 590px;
    left: 44px;
    width: 1112px;
    color: var(--body);
    font-size: 33px;
    line-height: 46px;
  }
  .intro p { margin: 0 0 46px; }
  .next-bar {
    position: absolute;
    bottom: 0; left: 0;
    width: 1200px;
    height: 152px;
    background: var(--chrome);
    color: var(--chrome-text);
    font-size: 44px;
    font-weight: 300;
    letter-spacing: 1px;
    display: flex;
    align-items: center;
    justify-content: center;
    gap: 18px;
  }
</style>
</head>
<body>
<main class="screen">
  <div class="status-bar">
    <div class="status-left">
      <div class="signal"><span class="on"></span><span class="on"></span><span class="on"></span><span></span><span></span></div>
      <span class="carrier">TELRA</span>
      <svg width="34" height="26" viewBox="0 0 34 26" aria-hidden="true">
        <path d="M3 9 A20 20 0 0 1 31 9" fill="none" stroke="#f2f3f4" stroke-width="3.5"/>
        <path d="M8 14 A13 13 0 0 1 26 14" fill="none" stroke="#f2f3f4" stroke-width="3.5"/>
        <circle cx="17" cy="21" r="3.5" fill="#f2f3f4"/>
      </svg>
    </div>
    <div class="status-time">4:21 PM</div>
    <div class="status-right">
      <svg width="18" height="30" viewBox="0 0 18 30" aria-hidden="true">
        <path d="M2 8 L15 21 L9 27 L9 3 L15 9 L2 22" fill="none" stroke="#f2f3f4" stroke-width="2.5"/>
      </svg>
      <span>100%</span>
      <div class="battery"><div class="battery-body"></div><div class="battery-tip"></div></div>
    </div>
  </div>

  <svg class="header-band" viewBox="0 0 1200 420" aria-hidden="true">
    <rect x="0" y="0" width="1200" height="232" fill="#5f6369"/>
    <path d="M422 231 A178 174 0 0 0 778 231 Z" fill="#5f6369"/>
    <g class="muted-icon" fill="none" stroke="#f2f3f4" stroke-width="6" stroke-linejoin="round" stroke-linecap="round">
      <path d="M558 250 L580 250 L618 217 L618 323 L580 290 L558 290 Z"/>
      <path d="M636 244 A34 34 0 0 1 636 298"/>
      <path d="M650 228 A54 54 0 0 1 650 314"/>
      <line x1="548" y1="214" x2="656" y2="326"/>
    </g>
  </svg>

  <h1 class="title">NOTIFICATIONS</h1>

  <section class="intro">
    <p>By enabling push notifications, we can keep you up to date with occasional notifications related to items you care about. Select the categories on the next screen and then authorize the push notifications.</p>
    <p>If you ever change your mind, you can adjust these options in the Settings menu of this app.</p>
  </section>

  <footer class="next-bar">
    <span>NEXT</span>
    <svg width="20" height="34" viewBox="0 0 20 34" aria-hidden="true">
      <path d="M4 4 L16 17 L4 30" fill="none" stroke="#f2f3f4" stroke-width="3"/>
    </svg>
  </footer>
</main>
</body>
</html>
```